Business Card Design

I need a bussiness card that have some picture of a van and lorry.
Updates

Hello I could ask you to print business cards and message to the home address?

Industry/Entity Type

Business

Contact Information for Business Card

K&M Transport LTD
truck and vans fridge
drivers recruitment
k.m-transport@quillmail.example
tel nr 07831452096

```html
<!DOCTYPE html>
<html lang="en">
<head>
<meta charset="utf-8">
<title>K&amp;M Transport LTD – Business Card</title>
<link rel="stylesheet" href="https://fonts.googleapis.com/css2?family=Questrial&family=Roboto:ital,wght@1,700&display=swap">
<style>
  :root {
    --matte: #000000;
    --card: #ffffff;
    --ink: #1a1a1a;
    --brand-purple: #4b2d8f;
    --band-text: #ffffff;
    --tag-bg: #0d0d0d;
    --tag-text: #e6e6e6;
  }
  * { margin: 0; padding: 0; box-sizing: border-box; }
  html, body {
    width: 1200px;
    height: 743px;
    overflow: hidden;
    background: var(--matte);
  }
  .card {
    position: absolute;
    left: 40px;
    top: 43px;
    width: 1122px;
    height: 657px;
    background: var(--card);
    overflow: hidden;
  }
  .photo {
    position: absolute;
    top: 172px;
    height: 190px;
  }
  .photo--truck {
    left: 0;
    width: 311px;
    background:
      linear-gradient(180deg, rgba(0,0,0,0) 55%, rgba(40,42,46,0.85) 100%),
      linear-gradient(160deg, #3a3f46 0%, #8d959e 30%, #c9ced3 48%, #6c737b 62%, #2b2e33 100%);
  }
  .photo--vans {
    left: 311px;
    width: 263px;
    background:
      linear-gradient(180deg, #5d8fc4 0%, #9cc0e2 40%, #cfdbe6 52%, #7c8793 62%, #3d434a 100%);
  }
  .tag {
    position: absolute;
    left: 0;
    top: 362px;
    width: 344px;
    height: 45px;
  }
  .tag__text {
    position: absolute;
    left: 36px;
    top: 368px;
    font-family: "Roboto", sans-serif;
    font-style: italic;
    font-weight: 700;
    font-size: 26px;
    color: var(--tag-text);
    letter-spacing: 0.5px;
  }
  .band {
    position: absolute;
    left: 589px;
    top: 172px;
    width: 533px;
    height: 192px;
  }
  .band__text {
    position: absolute;
    left: 604px;
    top: 246px;
    font-family: "Questrial", sans-serif;
    font-size: 31px;
    line-height: 36px;
    color: var(--band-text);
  }
  .contact {
    position: absolute;
    right: 76px;
    top: 497px;
    list-style: none;
    font-family: "Questrial", sans-serif;
    font-size: 33px;
    color: var(--ink);
  }
  .contact__item {
    display: flex;
    justify-content: flex-end;
    align-items: center;
    gap: 14px;
    height: 43px;
  }
  .contact__icon { width: 28px; height: 28px; }
</style>
</head>
<body>
  <main class="card">
    <div class="photo photo--truck" role="img" aria-label="Photo of a refrigerated lorry driving on a mountain road"></div>
    <div class="photo photo--vans" role="img" aria-label="Photo of two delivery vans driving on a city road"></div>

    <svg class="tag" viewBox="0 0 344 45" aria-hidden="true">
      <polygon points="0,0 344,0 291,45 0,45" fill="var(--tag-bg)"/>
    </svg>
    <span class="tag__text">Express Delivery</span>

    <svg class="band" viewBox="0 0 533 192" aria-hidden="true">
      <polygon points="0,70 372,70 496,0 533,0 533,192 0,192" fill="var(--brand-purple)"/>
    </svg>
    <p class="band__text">K&amp;M Transport LTD truck<br>and<br>vans fridge drivers recruitment</p>

    <ul class="contact">
      <li class="contact__item">
        <span>k.m-transport@quillmail.example</span>
        <svg class="contact__icon" viewBox="0 0 28 28" aria-hidden="true">
          <circle cx="14" cy="14" r="12" fill="none" stroke="var(--ink)" stroke-width="2"/>
          <circle cx="14" cy="14" r="4.5" fill="none" stroke="var(--ink)" stroke-width="2"/>
          <path d="M18.5 9.5 V16 a2.5 2.5 0 0 0 5 0 V14" fill="none" stroke="var(--ink)" stroke-width="2"/>
        </svg>
      </li>
      <li class="contact__item">
        <span>07831452096</span>
        <svg class="contact__icon" viewBox="0 0 28 28" aria-hidden="true">
          <circle cx="14" cy="14" r="12" fill="none" stroke="var(--ink)" stroke-width="2"/>
          <path d="M9.5 8 l3 -0.5 l1.5 3.5 l-2 1.5 a9 9 0 0 0 4 4 l1.5 -2 l3.5 1.5 l-0.5 3 c-6 0.5 -11.5 -5 -11 -11z" fill="var(--ink)"/>
        </svg>
      </li>
    </ul>
  </main>
</body>
</html>
```